Willowbay Dental Centre Tarrawin Opening special DL flyer

dl flyer design with opening special offers and services provide and the location we are in

opening special offer : exam, clean and flouride treatment for $129 or No Gap if with Health Insurance.
$99 mouth guards for footy season
Emergency Dental Appointments Available everyday!!!
Open on Saturdays

Services:
6 monthly Maintainence
CAD/CAM Dentistry
Conscious Sedation
Cosmetic Dentistry
Crowns and Bridges
Dental Implant
Fissure Sealants
Tresluxa
Periodontal Treatment
Root Canal Treatment
Teeth Whitening
Tooth Coloured Fillings
Tooth Replacement

Interest Free Payment Plans Available

Address: Willowbay Dental Centre Tarrawin
318D, Pellam Street, Tarrawin - 4611
Ph: 07-5019 4427
email: admin@willowbaydentalcentretarrawin.com.au
Website: www.willowbaydentalcentretarrawin.com.au

Opening Hours:
Mon/Wed 8:30AM - 5PM
Thursday 9AM - 7PM
Friday 9AM - 5PM
Saturday 9AM - 1PM

Target Market(s)

local community

Industry/Entity Type

Dental

Font styles to use
Serif

Requirements
Must have
• all the above details

```html
<!DOCTYPE html>
<html lang="en">
<head>
<meta charset="utf-8">
<title>Willowbay Dental Centre Tarrawin – Opening Special Flyer</title>
<link href="https://fonts.googleapis.com/css2?family=Signika:wght@400;600;700&family=Lato:wght@700&display=swap" rel="stylesheet">
<style>
  :root{
    --green:#6bc4a0;
    --lime:#bcd65a;
    --red:#b3202a;
    --ink:#222222;
    --white:#ffffff;
    --logo-bg:#1e1e1e;
  }
  *{margin:0;padding:0;box-sizing:border-box}
  html,body{width:1200px;height:1200px;overflow:hidden;background:var(--white)}
  body{position:relative;font-family:"Signika",sans-serif;color:var(--ink)}
  .flyer{position:absolute;top:198px;width:712px;height:1006px;transform:scale(.8);transform-origin:0 0;overflow:hidden;box-shadow:2px 3px 4px rgba(0,0,0,.35);background:var(--green)}
  .flyer--front{left:16px}
  .flyer--back{left:616px}
  .flyer__art{position:absolute;inset:0}
  .abs{position:absolute}
  .brand{left:25px;top:25px;width:135px;height:60px;background:var(--logo-bg);display:flex;align-items:center;justify-content:center;color:#d9d9d9;font-size:12.5px;font-weight:400;letter-spacing:.3px;text-align:center;line-height:1.15;padding:0 6px}
  .phone-top{left:25px;top:98px;font-size:24px;font-weight:600}
  .offer-label{left:22px;top:336px;font-family:"Lato",sans-serif;font-size:27px;color:var(--red);text-shadow:0 0 3px #fff,0 0 3px #fff}
  .deal{left:22px;top:430px;width:256px;text-align:center;font-weight:600}
  .deal__title{font-size:16.5px;line-height:19px}
  .deal__price{font-size:76px;font-weight:700;color:var(--red);line-height:80px;letter-spacing:-1px}
  .deal__note{font-size:16.5px;line-height:19px;margin-top:2px}
  .services{left:20px;top:665px;width:252px;height:310px;background:var(--lime);border:7px solid var(--white);border-radius:16px;padding:14px 0 0 20px}
  .services h2{font-size:28px;font-weight:600;color:var(--red);margin-bottom:14px;letter-spacing:.3px}
  .services ul{list-style:none}
  .services li{font-size:12.6px;font-weight:600;line-height:17.2px;padding-left:24px;position:relative}
  .services li::before{content:"";position:absolute;left:2px;top:5px;width:8px;height:9px;background:var(--ink);border-radius:3px 3px 1px 1px}
  .promo{left:282px;top:660px;width:400px;text-align:center}
  .promo__price{font-size:96px;font-weight:700;color:var(--red);line-height:100px}
  .promo__line{font-size:15.5px;font-weight:600;color:var(--white);line-height:20px}
  .promo__saturday{font-size:31px;font-weight:600;color:var(--red);margin-top:10px;letter-spacing:.3px}
  .hours-icon{left:300px;top:880px}
  .hours{left:400px;top:880px}
  .hours h3{font-size:29px;font-weight:600;margin-bottom:6px}
  .hours__grid{display:grid;grid-template-columns:124px auto;font-size:12.6px;font-weight:600;line-height:17px}
  .finance{left:25px;top:670px;width:440px;text-align:center;color:var(--red);font-size:40px;font-weight:700;line-height:54px}
  .contact{left:28px;top:800px;font-size:15px;font-weight:600;line-height:25px}
  .phone-big{left:25px;top:905px;font-size:45px;font-weight:700}
</style>
</head>
<body>

<section class="flyer flyer--front" aria-label="Opening special flyer, front">
  <svg class="flyer__art" viewBox="0 0 712 1006" width="712" height="1006">
    <rect width="712" height="1006" fill="var(--green)"/>
    <path role="img" aria-label="Photo of a smiling dentist with a hygienist examining a patient" d="M0 222 Q260 150 480 0 L712 0 L712 762 Q560 610 440 585 L280 480 L0 478 Z" fill="#e6e3df"/>
    <path d="M0 205 Q260 135 480 0" stroke="var(--lime)" stroke-width="14" fill="none"/>
    <path d="M0 478 L280 478" stroke="var(--lime)" stroke-width="22" fill="none"/>
    <path d="M420 580 Q570 630 712 770" stroke="var(--lime)" stroke-width="16" fill="none"/>
    <circle cx="150" cy="515" r="128" fill="var(--lime)"/>
    <circle cx="348" cy="565" r="90" fill="var(--lime)"/>
    <circle role="img" aria-label="Photo of a child at a dental check-up" cx="348" cy="565" r="80" fill="#c9b7a8"/>
    <rect y="990" width="712" height="16" fill="var(--lime)"/>
  </svg>
  <div class="abs brand">Willowbay Dental Centre</div>
  <p class="abs phone-top">Ph: 07-5019 4427</p>
  <p class="abs offer-label">Opening Special Offer:</p>
  <div class="abs deal">
    <p class="deal__title">EXAM, CLEAN AND<br>FLOURIDE TREATMENT</p>
    <p class="deal__price">$129</p>
    <p class="deal__note">NO GAP IF WITH<br>HEALTH INSURANCE.</p>
  </div>
  <div class="abs services">
    <h2>OUR SERVICE</h2>
    <ul>
      <li>6 monthly Maintainence</li>
      <li>CAD/CAM Dentistry</li>
      <li>Conscious Sedation</li>
      <li>Cosmetic Dentistry</li>
      <li>Crowns and Bridges</li>
      <li>Dental Implant</li>
      <li>Fissure Sealants</li>
      <li>Tresluxa</li>
      <li>Periodontal Treatment</li>
      <li>Root Canal Treatment</li>
      <li>Teeth Whitening</li>
      <li>Tooth Coloured Fillings</li>
      <li>Tooth Replacement</li>
    </ul>
  </div>
  <div class="abs promo">
    <p class="promo__price">$99</p>
    <p class="promo__line">MOUTH GUARDS FOR FOOTY SEASON</p>
    <p class="promo__line">Emergency Dental Appointments Available Everyday!!!</p>
    <p class="promo__saturday">OPEN ON SATURDAYS</p>
  </div>
  <svg class="abs hours-icon" width="90" height="90" viewBox="0 0 90 90" aria-hidden="true">
    <circle cx="45" cy="45" r="40" fill="none" stroke="var(--ink)" stroke-width="6"/>
    <path d="M45 18 V47 L62 64" fill="none" stroke="var(--ink)" stroke-width="6" stroke-linecap="round"/>
  </svg>
  <div class="abs hours">
    <h3>Opening Hours:</h3>
    <div class="hours__grid">
      <span>Mon/Wed 8:30AM</span><span>5PM Thursday 9AM - 7PM</span>
      <span>Friday 9AM - 5PM</span><span>Saturday 9AM - 1PM</span>
    </div>
  </div>
</section>

<section class="flyer flyer--back" aria-label="Opening special flyer, back">
  <svg class="flyer__art" viewBox="0 0 712 1006" width="712" height="1006">
    <rect width="712" height="1006" fill="var(--green)"/>
    <path role="img" aria-label="Photo of a smiling couple" d="M0 222 Q260 150 480 0 L712 0 L712 762 Q560 610 440 585 L280 480 L0 478 Z" fill="#ece6de"/>
    <path d="M0 205 Q260 135 480 0" stroke="var(--lime)" stroke-width="14" fill="none"/>
    <path d="M0 478 L280 478" stroke="var(--lime)" stroke-width="22" fill="none"/>
    <path d="M420 580 Q570 630 712 770" stroke="var(--lime)" stroke-width="16" fill="none"/>
    <circle cx="150" cy="515" r="128" fill="var(--lime)"/>
    <circle cx="348" cy="565" r="90" fill="var(--lime)"/>
    <circle role="img" aria-label="Photo of a child at a dental check-up" cx="348" cy="565" r="80" fill="#c9b7a8"/>
    <rect x="430" y="745" width="252" height="216" fill="var(--lime)"/>
    <rect role="img" aria-label="Street map showing the clinic location on Pellam Street" x="436" y="751" width="240" height="204" fill="#e2e2e2"/>
    <rect y="990" width="712" height="16" fill="var(--lime)"/>
  </svg>
  <div class="abs brand">Willowbay Dental Centre</div>
  <p class="abs phone-top">Ph: 07-5019 4427</p>
  <div class="abs deal">
    <p class="deal__title">EXAM, CLEAN AND<br>FLOURIDE TREATMENT</p>
    <p class="deal__price">$129</p>
    <p class="deal__note">NO GAP IF WITH<br>HEALTH INSURANCE.</p>
  </div>
  <p class="abs finance">Interest Free Payment<br>Plans Available</p>
  <div class="abs contact">
    <p>Address: Willowbay Dental Centre Tarrawin</p>
    <p>318D, Pellam Street, Tarrawin - 4611</p>
    <p>email: admin@willowbaydentalcentretarrawin.com.au</p>
    <p>Website: www.willowbaydentalcentretarrawin.com.au</p>
  </div>
  <p class="abs phone-big">Ph: 07-5019 4427</p>
</section>

</body>
</html>
```